Outstanding but small benefit administration firm serving large clients needs a website redesign

While the content on our current website is fine, when people arrive at our website, they know immediately that it was designed years ago. We are looking for something that can potentially be maintained on a content management system because we would like to hire a google certified expert to help with adwords and they often want to change the website or add meta data. We want the design to be mobile device friendly.

As for our company, we stress data accuracy, client customization and outstanding customer service. All of our competitors are large corporations (TelvarPrine, Doltry, Quimby, PayloomCrest, etc.). When we get a client, they stay with us. So many of our competitors do a horrible job with administration that many companies just think that's the way it is in this industry. We need to change that thinking! There is someone who can do it right at a reasonable price. We have very few out of scope fees. KWT knows how to make the transition from one administrator to us as painless as possible.

We like our current colors. We don't have a lot of time to write additional content.

Target Market(s)

Companies with 5,000 to 50,000 employees

Coding

Coded - Design and coding required

Number of Pages Required

2 page

Font styles to use
Sans Serif

Requirements
Must have
• If everything doesn't fit on one page, please show me what the second page would look like. For example, if there are See More links, what happens?
• We need for people to be able to submit short contact us with their company name as a required field.
• Ideally this website will be put on wordpress or something similar.
• Must be mobile device friendly.
Should not have
• Login, Register, Maps of our location, website search

```html
<!DOCTYPE html>
<html lang="en">
<head>
<meta charset="utf-8">
<title>Kestrel Welfare Trust</title>
<link rel="stylesheet" href="https://fonts.googleapis.com/css2?family=Lato:wght@300;400;700;900&display=swap">
<style>
:root{
  --green:#8dc63f;
  --lime:#c3d845;
  --blue:#4fc3f0;
  --ink:#222222;
  --text:#333333;
  --grey:#7f8285;
  --footer:#2b2b2b;
  --black:#000000;
  --white:#ffffff;
  --soft:#f3f4f1;
}
*{box-sizing:border-box;margin:0;padding:0}
html,body{width:1200px;height:2497px;overflow:hidden}
body{font-family:"Lato",Arial,sans-serif;color:var(--text);background:var(--white);position:relative}
a{text-decoration:none}

/* header */
.site-header{position:absolute;top:0;left:0;width:1200px;height:95px;border-top:4px solid #3a3a3a;background:var(--white)}
.brand{position:absolute;left:100px;top:28px;display:flex;align-items:center;gap:12px}
.brand-dot{width:26px;height:26px;border-radius:50%;background:var(--green)}
.brand-name{font-size:29px;font-weight:400;color:#555}
.header-contact{position:absolute;top:30px;display:flex;align-items:center;gap:12px;font-size:16px;color:#444}
.icon-badge{width:32px;height:32px;border-radius:50%;background:#555;display:flex;align-items:center;justify-content:center}

/* nav */
.main-nav{position:absolute;top:95px;left:0;width:1200px;height:42px;background:var(--black)}
.main-nav a{position:absolute;top:0;height:42px;line-height:42px;color:var(--white);font-size:15px;transform:translateX(-50%);text-align:center}
.main-nav a.active{background:var(--lime);color:var(--ink);width:95px}

/* hero */
.hero{position:absolute;top:137px;left:0;width:1200px;height:471px;background:linear-gradient(180deg,#6d7a85 0%,#9aa6b0 45%,#c9d0d6 75%,#8e9aa4 100%)}
.hero-title{position:absolute;top:188px;left:0;width:1200px;text-align:center;color:var(--white);font-size:31px;font-weight:700;line-height:43px;text-shadow:0 2px 4px rgba(0,0,0,.6)}
.hero-arrow{position:absolute;top:190px}

/* welcome */
.welcome{position:absolute;top:608px;left:0;width:1200px;height:317px}
.section-title{position:absolute;left:0;width:1200px;text-align:center;font-weight:400}
.welcome .section-title{top:50px;font-size:36px;color:var(--ink)}
.section-title span{color:var(--green)}
.divider{position:absolute;left:50%;transform:translateX(-50%);height:10px}
.divider::before{content:"";position:absolute;left:0;right:0;top:4px;height:1px;background:currentColor;opacity:.6}
.divider::after{content:"";position:absolute;left:50%;top:0;width:9px;height:9px;margin-left:-4.5px;border-radius:50%;background:var(--dot)}
.welcome-text{position:absolute;top:130px;left:105px;width:990px;text-align:center;font-size:13px;line-height:22px;color:#333}
.btn-more{position:absolute;top:237px;left:532px;width:130px;height:42px;background:var(--blue);color:var(--white);font-size:16px;font-weight:700;text-align:center;line-height:42px}

/* services */
.services{position:absolute;top:925px;left:0;width:1200px;height:468px;background:var(--white)}
.services-backdrop{position:absolute;top:0;left:0;width:1200px;height:361px;background:linear-gradient(180deg,#5e5a57 0%,#8c8884 50%,#a7a39f 100%)}
.services .section-title{top:48px;font-size:34px;color:var(--white);font-weight:300}
.service-card{position:absolute;top:150px;width:292px;height:290px;background:var(--white);border:2px solid #d6d6d6;padding:8px}
.service-card.featured{border-color:var(--green)}
.service-photo{width:100%;height:222px}
.service-caption{display:flex;align-items:center;gap:10px;padding:12px 0 0 8px;font-size:20px;font-weight:700;color:#777}
.service-card.featured .service-caption{color:var(--green)}
.caption-dot{width:14px;height:14px;border-radius:50%;background:currentColor}

/* testimonials */
.testimonials{position:absolute;top:1393px;left:0;width:1200px;height:494px;background:linear-gradient(135deg,#c9dc52 0%,#bfd443 50%,#c6da4b 100%)}
.testimonials .section-title{top:58px;font-size:34px;color:var(--black)}
.testimonial{position:absolute;top:140px;width:315px;text-align:center}
.avatar{width:82px;height:82px;border-radius:50%;margin:0 auto;border:4px solid var(--white);background:linear-gradient(180deg,#c9b3a0,#8a7361);box-shadow:0 0 0 1px #999}
.person-name{margin-top:22px;font-size:13px;font-weight:700;color:#222}
.person-role{font-size:13px;color:#222;margin-top:3px}
.quote-box{position:relative;margin-top:28px;height:122px;background:var(--white);box-shadow:0 3px 3px rgba(0,0,0,.25);padding:20px 24px;text-align:left;font-size:13px;line-height:20px;color:#222}
.quote-box::before{content:"";position:absolute;top:-12px;left:50%;margin-left:-13px;border-left:13px solid transparent;border-right:13px solid transparent;border-bottom:13px solid var(--white)}
.quote-mark{color:#bbb;font-size:22px;font-weight:900;margin-right:6px;vertical-align:-6px}

/* callback */
.callback{position:absolute;top:1887px;left:0;width:1200px;height:283px;background:var(--grey)}
.callback-title{position:absolute;top:44px;left:100px;font-size:36px;font-weight:300;line-height:44px;color:var(--white)}
.callback-text{position:absolute;top:148px;left:100px;width:290px;font-size:13px;line-height:21px;color:#e6e6e6}
.form-label{position:absolute;top:46px;left:459px;font-size:14px;color:var(--white)}
.field{position:absolute;width:308px;height:40px;background:var(--white);border:1px solid #ccc;font-family:inherit;font-size:12px;color:#333;padding:0 12px;outline:none}
.field::placeholder{color:#888}
.field.wide{width:641px}
.btn-submit{position:absolute;top:218px;left:459px;width:128px;height:40px;background:var(--black);color:var(--white);border:0;font-family:inherit;font-size:15px;font-weight:700;cursor:pointer}

/* footer */
.site-footer{position:absolute;top:2170px;left:0;width:1200px;height:275px;background:var(--footer)}
.footer-col{position:absolute;top:34px}
.footer-col h3{font-size:21px;font-weight:400;color:var(--green);padding-bottom:8px;border-bottom:1px solid #4a4a4a;width:160px}
.footer-sep{position:absolute;top:30px;width:1px;height:190px;background:#444}
.quick-links{list-style:none;margin-top:14px}
.quick-links li{font-size:13px;color:var(--white);height:28px;line-height:28px}
.quick-links li::before{content:"\2022";margin-right:6px}
.quick-links li.active{color:var(--green)}
.contact-row{display:flex;align-items:flex-start;gap:10px;font-size:13px;color:var(--white);margin-top:14px;line-height:18px}
.contact-row strong{color:var(--lime)}
.social-row{display:flex;align-items:center;gap:16px;margin-top:14px;font-size:13px;font-weight:700;color:var(--white);height:27px}
.social-dot{width:27px;height:27px;border-radius:50%;background:var(--lime)}
.footer-mark{position:absolute;top:110px;left:905px;width:240px;text-align:center;font-size:22px;font-weight:700;color:#555}
.copyright{position:absolute;top:2445px;left:0;width:1200px;height:52px;background:#111;color:#ccc;font-size:12px;text-align:center;line-height:52px}
.copyright strong{color:var(--white)}

/* second page: opened by Read More */
.detail-page{position:absolute;top:0;left:0;width:1200px;height:2497px;background:var(--white);display:none;z-index:10}
.detail-page:target{display:block}
.page-banner{position:absolute;top:137px;left:0;width:1200px;height:260px;background:linear-gradient(180deg,#6d7a85,#a9b3bb)}
.page-banner h1{position:absolute;top:82px;left:0;width:1200px;text-align:center;font-size:42px;font-weight:700;color:var(--white);text-shadow:0 2px 4px rgba(0,0,0,.5)}
.breadcrumb{position:absolute;top:146px;left:0;width:1200px;text-align:center;font-size:15px;color:var(--white)}
.breadcrumb span{color:var(--lime)}
.intro{position:absolute;top:397px;left:0;width:1200px;height:440px}
.intro .section-title{top:60px;font-size:36px;color:var(--ink)}
.intro-text{position:absolute;top:140px;left:150px;width:900px;text-align:center;font-size:16px;line-height:28px;color:#333}
.intro-text p+p{margin-top:18px}
.pillars{position:absolute;top:837px;left:0;width:1200px;height:440px;background:var(--soft)}
.pillars .section-title{top:50px;font-size:34px;color:var(--ink);font-weight:300}
.pillar{position:absolute;top:140px;width:320px;height:240px;background:var(--white);border-top:4px solid var(--green);padding:30px 28px;box-shadow:0 2px 4px rgba(0,0,0,.12)}
.pillar h3{display:flex;align-items:center;gap:10px;font-size:21px;font-weight:700;color:var(--green)}
.pillar p{margin-top:16px;font-size:15px;line-height:25px;color:#444}
.facts{position:absolute;top:1277px;left:0;width:1200px;height:420px}
.facts .section-title{top:60px;font-size:34px;color:var(--ink);font-weight:300}
.fact{position:absolute;top:150px;width:320px;text-align:center}
.fact strong{display:block;font-size:40px;font-weight:900;color:var(--green)}
.fact span{display:block;margin-top:10px;font-size:16px;line-height:24px;color:#444}
.cta{position:absolute;top:1697px;left:0;width:1200px;height:190px;background:linear-gradient(135deg,#c9dc52,#bfd443)}
.cta p{position:absolute;top:48px;left:0;width:1200px;text-align:center;font-size:28px;color:var(--black)}
.btn-back{position:absolute;top:108px;left:520px;width:160px;height:42px;background:var(--black);color:var(--white);font-size:15px;font-weight:700;text-align:center;line-height:42px}
</style>
</head>
<body>

<header class="site-header">
  <div class="brand"><span class="brand-dot"></span><span class="brand-name">Kestrel Welfare Trust</span></div>
  <div class="header-contact" style="left:703px">
    <span class="icon-badge"><svg width="16" height="16" viewBox="0 0 24 24"><path fill="#fff" d="M6.6 10.8a15 15 0 006.6 6.6l2.2-2.2c.3-.3.7-.4 1-.2 1.1.4 2.3.6 3.6.6.6 0 1 .4 1 1V20c0 .6-.4 1-1 1C10.6 21 3 13.4 3 4c0-.6.4-1 1-1h3.5c.6 0 1 .4 1 1 0 1.3.2 2.5.6 3.6.1.3 0 .7-.2 1z"/></svg></span>555-014-2271
  </div>
  <div class="header-contact" style="left:862px">
    <span class="icon-badge"><svg width="16" height="16" viewBox="0 0 24 24"><path fill="#fff" d="M3 5h18v14H3z"/><path fill="none" stroke="#555" stroke-width="2" d="M3 6l9 7 9-7"/></svg></span>info@kestrelwelfare.com
  </div>
</header>

<nav class="main-nav">
  <a class="active" href="#" style="left:122px">Home</a>
  <a href="#read-more" style="left:291px">Why KWT</a>
  <a href="#" style="left:472px">Services</a>
  <a href="#" style="left:661px">Technology</a>
  <a href="#" style="left:860px">Case Studies</a>
  <a href="#" style="left:1065px">Contact Us</a>
</nav>

<section class="hero">
  <div role="img" aria-label="Office desk with glasses, papers and a laptop keyboard, people in the background" style="position:absolute;inset:0"></div>
  <svg class="hero-arrow" style="left:52px" width="22" height="90" viewBox="0 0 22 90"><path d="M20 2L2 45l18 43" fill="none" stroke="#fff" stroke-width="2"/></svg>
  <svg class="hero-arrow" style="left:1126px" width="22" height="90" viewBox="0 0 22 90"><path d="M2 2l18 43L2 88" fill="none" stroke="#fff" stroke-width="2"/></svg>
  <h1 class="hero-title">We Focus On Large Clients With Complex Plans That<br>Need Both Flexibility And Sophistication</h1>
</section>

<section class="welcome">
  <h2 class="section-title">Welcome to <span>Kestrel Welfare Trust</span></h2>
  <div class="divider" style="top:104px;width:460px;color:#999;--dot:var(--blue)"></div>
  <p class="welcome-text">Lorem ipsum dolor sit amet, consectetur adipiscing elit. Sed vitae magna tellus. Aenean ante nunc, semper nec cursus non, rutrum ac eros. Vestibulum mattis justo ac dui bibendum consequat a ac ipsum. Praesent a arcu venenatis, auctor velit eu, suscipit libero. Quisque convallis, leo ac pharetra sagittis, ipsum arcu auctor urna, sit amet cursus risus augue in eros. Duis lacinia nisi vitae leo commodo, non finibus magna maximus. Sed posuere, neque eget bibendum pulvinar, ligula erat suscipit dolor, ut maximus arcu mi et tortor. Quisque imperdiet turpis et ligula mollis ultricies. Mauris lacinia rhoncus odio, at rutrum diam mollis eu.</p>
  <a class="btn-more" href="#read-more">Read More</a>
</section>

<section class="services">
  <div class="services-backdrop" role="img" aria-label="Close-up of a pen resting on documents"></div>
  <h2 class="section-title">OUR SERVICES</h2>
  <div class="divider" style="top:92px;width:236px;color:#ddd;--dot:#fff"></div>
  <div class="service-card featured" style="left:100px">
    <div class="service-photo" role="img" aria-label="Hand pointing at a bar chart on a tablet" style="background:linear-gradient(160deg,#c7b7a8,#6e7f9a)"></div>
    <div class="service-caption"><span class="caption-dot"></span>Data Accuracy</div>
  </div>
  <div class="service-card" style="left:455px">
    <div class="service-photo" role="img" aria-label="Business people shaking hands across a table" style="background:linear-gradient(160deg,#8a8f96,#3d3f44)"></div>
    <div class="service-caption"><span class="caption-dot"></span>Client Customization</div>
  </div>
  <div class="service-card" style="left:808px">
    <div class="service-photo" role="img" aria-label="Support team members wearing headsets" style="background:linear-gradient(160deg,#e2ddd8,#6d6a6a)"></div>
    <div class="service-caption"><span class="caption-dot"></span>Customer Service</div>
  </div>
</section>

<section class="testimonials">
  <h2 class="section-title">CLIENTS TESTIMONIALS</h2>
  <div class="divider" style="top:106px;width:476px;color:#333;--dot:#111"></div>
  <div class="testimonial" style="left:100px">
    <div class="avatar" role="img" aria-label="Portrait of client Arlo Fenwick"></div>
    <div class="person-name">Mr Arlo Fenwick</div>
    <div class="person-role">Director, Lorem Ipsum</div>
    <div class="quote-box"><span class="quote-mark">&ldquo;</span>Lorem ipsum dolor sit amet, consectetur adipiscing elit. Sed vitae magna tellus. Aenean ante nunc, semper nec cursus non, rutrum ac eros. Vestibulum mattis justo ac dui.</div>
  </div>
  <div class="testimonial" style="left:442px">
    <div class="avatar" role="img" aria-label="Portrait of client Lena Harrow"></div>
    <div class="person-name">Miss Lena Harrow</div>
    <div class="person-role">Director, Lorem Ipsum</div>
    <div class="quote-box"><span class="quote-mark">&ldquo;</span>Lorem ipsum dolor sit amet, consectetur adipiscing elit. Sed vitae magna tellus. Aenean ante nunc, semper nec cursus non, rutrum ac eros. Vestibulum mattis justo ac dui.</div>
  </div>
  <div class="testimonial" style="left:785px">
    <div class="avatar" role="img" aria-label="Portrait of client Tom Brisco"></div>
    <div class="person-name">Mr Tom Brisco</div>
    <div class="person-role">Director, Lorem Ipsum</div>
    <div class="quote-box"><span class="quote-mark">&ldquo;</span>Lorem ipsum dolor sit amet, consectetur adipiscing elit. Sed vitae magna tellus. Aenean ante nunc, semper nec cursus non, rutrum ac eros. Vestibulum mattis justo ac dui.</div>
  </div>
</section>

<section class="callback">
  <h2 class="callback-title">Request<br>A Call Back</h2>
  <p class="callback-text">Duis autem vel eum iriure dolormi opl inmokl hendi rerit in vulpu tateml velitm essemol mo molestiel consequat uat, velmi illum dolor eokf no atn nulla more facilisis</p>
  <form class="callback-form" action="#" method="post">
    <div class="form-label">Please fill up bellow form</div>
    <input class="field" style="top:76px;left:459px" type="text" name="name" placeholder="Name">
    <input class="field" style="top:76px;left:792px" type="text" name="company" placeholder="Company Name *" required>
    <input class="field" style="top:122px;left:459px" type="tel" name="phone" placeholder="Phone">
    <input class="field" style="top:122px;left:792px" type="email" name="email" placeholder="Email">
    <input class="field wide" style="top:168px;left:459px" type="text" name="message" placeholder="Message">
    <button class="btn-submit" type="submit">SUBMIT</button>
  </form>
</section>

<footer class="site-footer">
  <div class="footer-col" style="left:98px">
    <h3>Quick Links</h3>
    <ul class="quick-links">
      <li class="active">Home</li><li>Why KWT</li><li>Services</li><li>Technology</li><li>Case Studies</li><li>Contact Us</li>
    </ul>
  </div>
  <div class="footer-sep" style="left:611px"></div>
  <div class="footer-col" style="left:333px">
    <h3>Contact Details</h3>
    <div class="contact-row"><svg width="12" height="16" viewBox="0 0 12 16"><path fill="#c3d845" d="M6 0a6 6 0 00-6 6c0 4.5 6 10 6 10s6-5.5 6-10a6 6 0 00-6-6zm0 8.5A2.5 2.5 0 116 3.5a2.5 2.5 0 010 5z"/></svg><div><strong>Kestrel Welfare Trust</strong><br>4820 Millbrook Ave<br>Fairview Twp., MI 48000</div></div>
    <div class="contact-row"><svg width="14" height="14" viewBox="0 0 24 24"><path fill="#c3d845" d="M6.6 10.8a15 15 0 006.6 6.6l2.2-2.2c.3-.3.7-.4 1-.2 1.1.4 2.3.6 3.6.6.6 0 1 .4 1 1V20c0 .6-.4 1-1 1C10.6 21 3 13.4 3 4c0-.6.4-1 1-1h3.5c.6 0 1 .4 1 1 0 1.3.2 2.5.6 3.6.1.3 0 .7-.2 1z"/></svg>555-014-2271</div>
    <div class="contact-row"><svg width="14" height="14" viewBox="0 0 14 14"><rect x="1" y="5" width="12" height="7" fill="#c3d845"/><rect x="3" y="1" width="8" height="4" fill="#c3d845"/></svg>555-014-2284</div>
    <div class="contact-row"><svg width="14" height="12" viewBox="0 0 14 12"><rect x="0" y="1" width="14" height="10" fill="#c3d845"/><path d="M0 2l7 5 7-5" fill="none" stroke="#2b2b2b" stroke-width="1.2"/></svg>info@kestrelwelfare.com</div>
  </div>
  <div class="footer-sep" style="left:882px"></div>
  <div class="footer-col" style="left:670px">
    <h3>Follow Us</h3>
    <div class="social-row"><span class="social-dot"></span>Like Us</div>
    <div class="social-row"><span class="social-dot"></span>Follow Us</div>
    <div class="social-row"><span class="social-dot"></span>Connect Us</div>
    <div class="social-row"><span class="social-dot"></span>Add to Circle</div>
  </div>
  <div class="footer-mark">Kestrel Welfare Trust</div>
</footer>

<div class="copyright">Copyright &copy; 2016 <strong>Kestrel Welfare Trust.</strong> All rights reserved.</div>

<!-- Second page: Why KWT, opened from Read More -->
<section class="detail-page" id="read-more">
  <header class="site-header">
    <div class="brand"><span class="brand-dot"></span><span class="brand-name">Kestrel Welfare Trust</span></div>
    <div class="header-contact" style="left:703px"><span class="icon-badge"><svg width="16" height="16" viewBox="0 0 24 24"><path fill="#fff" d="M6.6 10.8a15 15 0 006.6 6.6l2.2-2.2c.3-.3.7-.4 1-.2 1.1.4 2.3.6 3.6.6.6 0 1 .4 1 1V20c0 .6-.4 1-1 1C10.6 21 3 13.4 3 4c0-.6.4-1 1-1h3.5c.6 0 1 .4 1 1 0 1.3.2 2.5.6 3.6.1.3 0 .7-.2 1z"/></svg></span>555-014-2271</div>
    <div class="header-contact" style="left:862px"><span class="icon-badge"><svg width="16" height="16" viewBox="0 0 24 24"><path fill="#fff" d="M3 5h18v14H3z"/><path fill="none" stroke="#555" stroke-width="2" d="M3 6l9 7 9-7"/></svg></span>info@kestrelwelfare.com</div>
  </header>
  <nav class="main-nav">
    <a href="#" style="left:122px">Home</a>
    <a class="active" href="#read-more" style="left:291px;width:110px">Why KWT</a>
    <a href="#" style="left:472px">Services</a>
    <a href="#" style="left:661px">Technology</a>
    <a href="#" style="left:860px">Case Studies</a>
    <a href="#" style="left:1065px">Contact Us</a>
  </nav>
  <div class="page-banner" role="img" aria-label="Office desk scene in soft blue-grey tones">
    <h1>Why Kestrel Welfare Trust</h1>
    <div class="breadcrumb">Home / <span>Why KWT</span></div>
  </div>

  <div class="intro">
    <h2 class="section-title">Administration <span>Done Right</span></h2>
    <div class="divider" style="top:114px;width:400px;color:#999;--dot:var(--blue)"></div>
    <div class="intro-text">
      <p>Many companies believe poor benefit administration is simply the way this industry works. Our large competitors have made that the norm. We are here to change that thinking.</p>
      <p>Kestrel Welfare Trust is a small, focused firm serving large clients with complex plans. We deliver careful administration at a reasonable price, with very few out-of-scope fees.</p>
      <p>When a client joins us, they stay with us.</p>
    </div>
  </div>

  <div class="pillars">
    <h2 class="section-title">WHAT WE STAND FOR</h2>
    <div class="divider" style="top:98px;width:300px;color:#999;--dot:var(--green)"></div>
    <div class="pillar" style="left:100px"><h3><span class="caption-dot"></span>Data Accuracy</h3><p>Every record is checked and reconciled, so your plans run on numbers you can trust.</p></div>
    <div class="pillar" style="left:440px"><h3><span class="caption-dot"></span>Client Customization</h3><p>Flexible, sophisticated setups built around the way your plans actually work.</p></div>
    <div class="pillar" style="left:780px"><h3><span class="caption-dot"></span>Customer Service</h3><p>Real people who know your account and answer quickly, every single time.</p></div>
  </div>

  <div class="facts">
    <h2 class="section-title">WHO WE SERVE</h2>
    <div class="divider" style="top:108px;width:260px;color:#999;--dot:var(--green)"></div>
    <div class="fact" style="left:100px"><strong>5,000&ndash;50,000</strong><span>Employees at the companies<br>we support</span></div>
    <div class="fact" style="left:440px"><strong>Few Fees</strong><span>Very few out-of-scope charges<br>at a reasonable price</span></div>
    <div class="fact" style="left:780px"><strong>Easy Switch</strong><span>A transition from your current<br>administrator made painless</span></div>
  </div>

  <div class="cta">
    <p>Ready to see benefit administration done right?</p>
    <a class="btn-back" href="#">Back to Home</a>
  </div>

  <section class="callback">
    <h2 class="callback-title">Request<br>A Call Back</h2>
    <p class="callback-text">Duis autem vel eum iriure dolormi opl inmokl hendi rerit in vulpu tateml velitm essemol mo molestiel consequat uat, velmi illum dolor eokf no atn nulla more facilisis</p>
    <form class="callback-form" action="#" method="post">
      <div class="form-label">Please fill up bellow form</div>
      <input class="field" style="top:76px;left:459px" type="text" name="name" placeholder="Name">
      <input class="field" style="top:76px;left:792px" type="text" name="company" placeholder="Company Name *" required>
      <input class="field" style="top:122px;left:459px" type="tel" name="phone" placeholder="Phone">
      <input class="field" style="top:122px;left:792px" type="email" name="email" placeholder="Email">
      <input class="field wide" style="top:168px;left:459px" type="text" name="message" placeholder="Message">
      <button class="btn-submit" type="submit">SUBMIT</button>
    </form>
  </section>

  <footer class="site-footer">
    <div class="footer-col" style="left:98px">
      <h3>Quick Links</h3>
      <ul class="quick-links">
        <li>Home</li><li class="active">Why KWT</li><li>Services</li><li>Technology</li><li>Case Studies</li><li>Contact Us</li>
      </ul>
    </div>
    <div class="footer-sep" style="left:611px"></div>
    <div class="footer-col" style="left:333px">
      <h3>Contact Details</h3>
      <div class="contact-row"><svg width="12" height="16" viewBox="0 0 12 16"><path fill="#c3d845" d="M6 0a6 6 0 00-6 6c0 4.5 6 10 6 10s6-5.5 6-10a6 6 0 00-6-6zm0 8.5A2.5 2.5 0 116 3.5a2.5 2.5 0 010 5z"/></svg><div><strong>Kestrel Welfare Trust</strong><br>4820 Millbrook Ave<br>Fairview Twp., MI 48000</div></div>
      <div class="contact-row"><svg width="14" height="14" viewBox="0 0 24 24"><path fill="#c3d845" d="M6.6 10.8a15 15 0 006.6 6.6l2.2-2.2c.3-.3.7-.4 1-.2 1.1.4 2.3.6 3.6.6.6 0 1 .4 1 1V20c0 .6-.4 1-1 1C10.6 21 3 13.4 3 4c0-.6.4-1 1-1h3.5c.6 0 1 .4 1 1 0 1.3.2 2.5.6 3.6.1.3 0 .7-.2 1z"/></svg>555-014-2271</div>
      <div class="contact-row"><svg width="14" height="14" viewBox="0 0 14 14"><rect x="1" y="5" width="12" height="7" fill="#c3d845"/><rect x="3" y="1" width="8" height="4" fill="#c3d845"/></svg>555-014-2284</div>
      <div class="contact-row"><svg width="14" height="12" viewBox="0 0 14 12"><rect x="0" y="1" width="14" height="10" fill="#c3d845"/><path d="M0 2l7 5 7-5" fill="none" stroke="#2b2b2b" stroke-width="1.2"/></svg>info@kestrelwelfare.com</div>
    </div>
    <div class="footer-sep" style="left:882px"></div>
    <div class="footer-col" style="left:670px">
      <h3>Follow Us</h3>
      <div class="social-row"><span class="social-dot"></span>Like Us</div>
      <div class="social-row"><span class="social-dot"></span>Follow Us</div>
      <div class="social-row"><span class="social-dot"></span>Connect Us</div>
      <div class="social-row"><span class="social-dot"></span>Add to Circle</div>
    </div>
    <div class="footer-mark">Kestrel Welfare Trust</div>
  </footer>
  <div class="copyright">Copyright &copy; 2016 <strong>Kestrel Welfare Trust.</strong> All rights reserved.</div>
</section>

</body>
</html>
```